TRU PEAK POWER.

I'd like my business logo.
contact name: Desmond Halvik
phone:0438275160
email: info@trupeakpower.net.au
website: www.trupeakpower.net.au

services:
solar
battery storage
LED lighting
energy saving solutions
general electrical
I'd like the design to look professional

Target Market(s)

Everyone

Industry/Entity Type

Business

Contact Information for Business Card

as described above

Requirements
Must have
• Id like the colours and the design to work well with my logo.

```html
<!DOCTYPE html>
<html lang="en">
<head>
<meta charset="utf-8">
<title>Tru Peak Power – Business Card</title>
<link href="https://fonts.googleapis.com/css2?family=Open+Sans:wght@400;600;700&display=swap" rel="stylesheet">
<style>
  :root {
    --page-bg: #ecebe6;
    --card-white: #f7f7f7;
    --green-deep: #7cbf35;
    --green-mid: #9ad04c;
    --green-light: #d6ec95;
    --brand-green: #6fb93a;
    --sun-orange: #f4a81d;
    --text-on-green: #ffffff;
  }
  * { box-sizing: border-box; margin: 0; padding: 0; }
  html, body {
    width: 1200px; height: 1023px; overflow: hidden;
    background: var(--page-bg);
    font-family: "Open Sans", Arial, sans-serif;
  }
  .card {
    position: absolute; left: 100px; top: 211px;
    width: 1000px; height: 600px;
    border-radius: 26px; overflow: hidden;
    background: var(--card-white);
    box-shadow: 0 18px 40px rgba(0,0,0,.18);
  }
  .card__band {
    position: absolute; left: 0; right: 0; top: 330px; bottom: 0;
    background: linear-gradient(90deg, var(--green-deep) 0%, var(--green-mid) 35%, var(--green-light) 58%, var(--green-mid) 70%, var(--green-deep) 100%);
  }
  .card__column {
    position: absolute; left: 690px; right: 0; top: 0; bottom: 0;
    background: linear-gradient(180deg, var(--green-mid) 0%, var(--green-deep) 100%);
  }
  .brand {
    position: absolute; left: 90px; top: 130px;
    display: flex; align-items: center; gap: 20px;
  }
  .brand__dot {
    width: 56px; height: 56px; border-radius: 50%;
    background: var(--sun-orange);
  }
  .brand__name {
    font-weight: 700; font-size: 48px; letter-spacing: 1px;
    color: var(--brand-green);
  }
  .contact {
    position: absolute; left: 56px; top: 372px;
    color: var(--text-on-green);
  }
  .contact__name {
    display: flex; align-items: center; gap: 12px;
    font-weight: 700; font-size: 36px; margin-bottom: 20px;
  }
  .contact__line {
    display: flex; align-items: center; gap: 12px;
    font-size: 24px; line-height: 38px;
  }
  .icon { width: 24px; height: 24px; flex: none; }
  .icon--lg { width: 30px; height: 30px; }
  .services {
    position: absolute; left: 690px; right: 32px; top: 60px;
    text-align: right; color: var(--text-on-green);
  }
  .services__title {
    display: inline-block; font-size: 28px; font-weight: 600;
    border-bottom: 2px solid var(--text-on-green);
    padding-bottom: 2px; margin-bottom: 14px;
  }
  .services__list { list-style: none; font-size: 21px; line-height: 40px; white-space: nowrap; }
  .services__list li::after { content: " \2022"; }
</style>
</head>
<body>
  <div class="card">
    <div class="card__band"></div>
    <div class="card__column"></div>

    <div class="brand">
      <span class="brand__dot"></span>
      <span class="brand__name">TRU PEAK POWER</span>
    </div>

    <div class="contact">
      <div class="contact__name">
        <svg class="icon icon--lg" viewBox="0 0 24 24"><circle cx="12" cy="12" r="11" fill="#fff"/><circle cx="12" cy="9" r="3.6" fill="#8cc63f"/><path d="M5.5 18.5c1.5-3.2 4-4.5 6.5-4.5s5 1.3 6.5 4.5" fill="#8cc63f"/></svg>
        Desmond Halvik
      </div>
      <div class="contact__line">
        <svg class="icon" viewBox="0 0 24 24"><circle cx="12" cy="12" r="10.5" fill="none" stroke="#fff" stroke-width="1.6"/><path d="M9 7l1.6 2.6-1.2 1.2a7 7 0 003 3l1.2-1.2L16.2 14l-1 2.2c-4.5-.4-7.7-3.7-8.2-8.2z" fill="#fff"/></svg>
        0438275160
      </div>
      <div class="contact__line">
        <svg class="icon" viewBox="0 0 24 24"><rect x="2" y="5" width="20" height="14" fill="#fff"/><path d="M2 5l10 8 10-8" fill="none" stroke="#8cc63f" stroke-width="1.6"/></svg>
        info@trupeakpower.net.au
      </div>
      <div class="contact__line">
        <svg class="icon" viewBox="0 0 24 24" fill="none" stroke="#fff" stroke-width="1.6"><circle cx="12" cy="12" r="10"/><ellipse cx="12" cy="12" rx="4.5" ry="10"/><path d="M2 12h20M4 7h16M4 17h16"/></svg>
        www.trupeakpower.net.au
      </div>
    </div>

    <div class="services">
      <div class="services__title">Services</div>
      <ul class="services__list">
        <li>Solar</li>
        <li>LED lighting</li>
        <li>Battery Storage</li>
        <li>General Electrical</li>
        <li>Energy Saving Solutions</li>
      </ul>
    </div>
  </div>
</body>
</html>
```